Redesign This Psychology Website

We would like a slight redesign of this successful psychology (relationship counselling) website:

www.TheLumaHaven.com.au

We are updating the website, and we'd like a slight refresh of the design and style.

Please keep to very similar colours, and use the same logo. We're looking for around 10 page templates, however the main one is the home page.

Keep in mind, this website already converts quite well, so we want a new, fresh design in keeping with this one. Please don't bother designing something too extremely different.

thanks :)
Updates

Target Market(s)

couples who are looking for relationship counselling. Men and women, 25 - 70, across Australia

Industry/Entity Type

Psychology

Number of Pages Required

5+ page

Font styles to use
Sans Serif

Colors
87cfc6
b7a5cd
ec1f27
ffffff
cee9f5

Requirements
Must have
• a similar look to the current design, just looking for a slight refresh.
• Search bar
• Areas for lots of photos
• same logo
• lots of content areas
Nice to have
• great content areas, where we can display a lot of content and our areas.
Should not have
• no colors like orange, etc.
• should not have a totally different feel.

```html
<!DOCTYPE html>
<html lang="en">
<head>
<meta charset="utf-8">
<title>The Luma Haven – Relationship Counselling</title>
<link rel="stylesheet" href="https://fonts.googleapis.com/css2?family=Lato:ital,wght@0,400;0,700;0,900;1,400;1,700&family=Dancing+Script:wght@500&display=swap">
<style>
:root{
  --teal:#87cfc6;
  --teal-dark:#1d7f8e;
  --lilac:#b7a5cd;
  --red:#ec1f27;
  --sky:#cee9f5;
  --white:#ffffff;
  --ink:#3d3d3d;
  --grey:#f2f2f2;
  --line:#dcdcdc;
}
*{box-sizing:border-box;margin:0;padding:0}
html,body{width:1200px;height:3822px;overflow:hidden}
body{font-family:'Lato',sans-serif;color:var(--ink);background:var(--white);font-size:11px;line-height:1.55}
.wrap{width:890px;margin:0 auto;position:relative}
a{color:inherit;text-decoration:none}

.topbar{height:36px;background:var(--teal-dark);color:var(--white);font-size:10px;font-weight:700;letter-spacing:.3px}
.topbar .wrap{display:flex;align-items:center;height:36px;justify-content:space-between}
.topbar .links span{margin-right:14px}
.topbar .call{font-size:12px;font-weight:900}
.topbar .social{display:flex;gap:6px;margin-left:18px}
.topbar .social i{width:14px;height:14px;border-radius:50%;background:var(--white);opacity:.8;display:block}
.topbar .right{display:flex;align-items:center}

.header{height:76px;border-bottom:1px solid var(--line)}
.header .wrap{display:flex;align-items:center;height:76px;justify-content:space-between}
.brand{display:flex;align-items:center;gap:10px}
.brand-dot{width:34px;height:34px;border-radius:50%;background:var(--teal)}
.brand-name{font-size:22px;font-weight:700;color:var(--teal-dark);line-height:1}
.brand-tag{font-size:9px;color:var(--teal-dark)}
.nav{display:flex;align-items:center;gap:20px;font-size:11px;font-weight:700;color:#555}
.search{display:flex;align-items:center;gap:6px;margin-left:12px}
.search span{width:130px;height:24px;border:1px solid var(--line);font-size:9px;color:#aaa;padding:5px 8px;font-weight:400}

.hero{height:494px;background:linear-gradient(90deg,#e9f2f6 0%,#dfe9ef 45%,#d8b597 70%,#b4865f 100%);position:relative}
.hero-video{position:absolute;left:158px;top:112px;width:555px;height:296px;background:linear-gradient(135deg,#cfe2ee,#a8c8dc 55%,#e8d3c0);border:4px solid var(--white);display:flex;align-items:center;justify-content:center}
.play{width:54px;height:38px;border-radius:8px;background:rgba(30,30,30,.8);display:flex;align-items:center;justify-content:center}

.tabs{height:97px;background:var(--sky)}
.tabs .wrap{display:flex;height:97px;align-items:stretch}
.tab{display:flex;align-items:center;justify-content:center;text-align:center;padding:0 22px;font-size:12px;font-weight:700;color:var(--teal-dark);text-transform:uppercase;border-right:1px solid #b9dbe9}
.tab.active{background:var(--red);color:var(--white);width:127px}

.types{height:418px;background:var(--grey);padding-top:61px}
.types .wrap{display:flex;justify-content:space-between}
.type{width:205px;text-align:center}
.type-photo{width:150px;height:150px;border-radius:50%;margin:0 auto 14px;border:5px solid var(--white);box-shadow:0 1px 4px rgba(0,0,0,.15)}
.type h3{color:var(--red);font-size:17px;font-weight:700;line-height:1.15;text-transform:uppercase}
.type .need{font-size:14px;margin:4px 0 6px}
.type p{font-size:12px;line-height:1.45}

.main{display:flex;justify-content:space-between;padding-top:56px;height:2293px}
.content{width:600px}
.side{width:242px}
h2{color:var(--teal-dark);font-size:19px;font-weight:700;margin-bottom:12px}
.content p{margin-bottom:11px}
.content strong{color:var(--teal-dark)}
.script{font-family:'Dancing Script',cursive;font-size:30px;font-weight:500;color:var(--teal-dark);margin:26px 0 8px}
.checks{list-style:none;margin-bottom:14px}
.checks li{padding-left:14px;position:relative;line-height:1.6}
.checks li:before{content:"✓";position:absolute;left:0;color:var(--teal-dark)}
.note{font-style:italic;color:var(--teal-dark)}
.ctas{display:flex;gap:14px;margin:16px 0 36px}
.cta{flex:1;height:70px;border:1px solid var(--line);display:flex;align-items:center;gap:12px;padding:6px}
.cta-photo{width:70px;height:56px;background:linear-gradient(135deg,#e8c8ad,#c79a7b)}
.cta span{flex:1;font-style:italic;font-size:14px;color:var(--teal-dark)}
.arrow{width:20px;height:20px;border-radius:50%;background:var(--red);flex:none;display:flex;align-items:center;justify-content:center}
.locs{display:grid;grid-template-columns:190px 190px;margin:4px 0 14px 14px;list-style:none}
.locs li{color:var(--red);line-height:1.7}
.locs b{color:var(--teal-dark)}
.photo-wide{width:275px;height:145px;background:linear-gradient(135deg,#d9c0a8,#a57f60);margin:40px 0 44px}
.photo-small{width:205px;height:78px;background:linear-gradient(135deg,#e9d7c4,#c7a386);margin:10px auto 40px;border-radius:4px}
.italic-h{font-style:italic;color:var(--teal-dark);font-size:19px;font-weight:700;margin-bottom:12px}
.plain{list-style:none;margin:0 0 12px 14px;color:var(--teal-dark)}

.finder{height:230px;background:var(--sky);border:1px solid #a9d0e0;padding:14px 16px;margin-bottom:36px}
.finder h4{color:var(--red);font-size:14px;text-align:center;font-weight:400;line-height:1.2;margin-bottom:10px}
.row{display:flex;align-items:center;gap:8px;margin-bottom:8px;font-size:9px}
.row label{width:56px;text-align:right}
.row span{flex:1;height:18px;background:var(--white);border:1px solid var(--line)}
.finder .or{color:var(--red);text-align:center;font-weight:700;font-size:10px;margin-bottom:6px}
.btn{display:inline-block;background:var(--red);color:var(--white);font-weight:700;font-size:10px;padding:5px 14px}
.ad{height:188px;background:linear-gradient(135deg,#f6dcd0,#e6b9a4);position:relative;margin-bottom:10px}
.ad h5{position:absolute;left:12px;top:14px;color:var(--red);font-style:italic;font-size:17px;line-height:1.15;font-weight:900}
.ad-bar{position:absolute;left:0;right:0;bottom:0;background:var(--red);color:var(--white);font-size:10px;padding:4px 8px;line-height:1.3}
.ad.gp{height:166px;background:linear-gradient(135deg,#eef3f6,#cfdde6)}
.ad.gp h5{color:var(--teal-dark);left:auto;right:10px;top:40px;width:130px}
.side h6{color:var(--red);font-size:15px;font-style:italic;font-weight:700;margin:16px 0 8px}
.badges{display:grid;grid-template-columns:repeat(3,1fr);gap:8px}
.badges i{display:block;height:26px;border-radius:4px}
.more{text-align:center;color:var(--red);font-size:10px;margin:8px 0}
.rebate{font-size:13px;line-height:1.3}
.rebate b{color:var(--red)}
.bar-btn{background:var(--red);color:var(--white);font-size:11px;padding:4px 8px;margin:8px 0 14px}
.side .sub{color:var(--teal-dark);font-size:12px;font-weight:700;font-style:italic}
.vid{height:148px;background:linear-gradient(135deg,#d8c4b3,#a98d78);margin:8px 0 58px;display:flex;align-items:center;justify-content:center}
.vid i{width:36px;height:36px;border-radius:50%;background:var(--red);display:block}
.blog-head{font-size:11px;color:#666;border-top:1px solid var(--line);padding-top:10px}
.blog-head b{display:block;color:var(--red);font-size:16px;font-style:italic}
.post{display:flex;gap:10px;height:99px;padding-top:12px;border-bottom:1px solid #eee}
.post .thumb{width:80px;height:78px;background:linear-gradient(135deg,#e2c6ae,#b48c6e);flex:none}
.post b{display:block;color:var(--red);font-style:italic;font-size:12px;line-height:1.25}
.post small{display:block;color:#888;font-size:9px}
.post em{color:var(--teal-dark);font-size:9px}

.features{height:230px;padding-top:18px}
.features .wrap{display:grid;grid-template-columns:repeat(3,1fr);gap:22px 22px}
.feat{display:flex;align-items:center;gap:10px;height:90px;border:1px solid var(--line);padding-right:8px}
.feat .ph{width:110px;height:88px;background:linear-gradient(135deg,#e6cbb5,#b58e70)}
.feat span{flex:1;color:var(--red);font-style:italic;font-weight:700;font-size:15px;line-height:1.2}

.footer{height:178px;background:var(--sky) repeating-linear-gradient(45deg,rgba(255,255,255,.25) 0 2px,transparent 2px 6px);padding-top:18px;font-size:11px;color:var(--teal-dark)}
.footer .top{display:flex;justify-content:space-between;align-items:flex-start}
.footer .name{font-weight:700}
.login{display:flex;gap:8px;align-items:center;font-size:10px;font-weight:700;margin-top:10px}
.login span{width:110px;height:20px;background:var(--white);border:1px solid var(--line);font-weight:400;color:#aaa;padding:3px 6px;font-size:9px}
.login .go{width:28px;background:var(--teal);border:none}
.footer .copy{margin-top:68px;font-size:10px;line-height:1.5}
</style>
</head>
<body>

<div class="topbar"><div class="wrap">
  <div class="links"><span>JOIN OUR ASSOCIATE PROGRAM</span><span>MARRIAGE COUNSELLING</span><span>RELATIONSHIP COUNSELLING</span></div>
  <div class="right"><span class="call">CALL US ON 1300 555 014</span><div class="social"><i></i><i></i><i></i></div></div>
</div></div>

<header class="header"><div class="wrap">
  <div class="brand"><span class="brand-dot"></span><div><div class="brand-name">The Luma Haven</div><div class="brand-tag">helping you create loving relationships</div></div></div>
  <nav class="nav"><a>HOME</a><a>ABOUT</a><a>RESOURCES</a><a>BLOG</a><a>SHOP</a><a>CART</a>
    <div class="search"><span>Search here</span>
      <svg width="16" height="16" viewBox="0 0 16 16"><circle cx="6.5" cy="6.5" r="5" fill="none" stroke="#1d7f8e" stroke-width="2"/><line x1="10" y1="10" x2="15" y2="15" stroke="#1d7f8e" stroke-width="2"/></svg></div>
  </nav>
</div></header>

<section class="hero" role="img" aria-label="Smiling couple embracing">
  <div class="hero-video" role="img" aria-label="Video of a counsellor introducing the centre">
    <div class="play"><svg width="16" height="18" viewBox="0 0 16 18"><path d="M0 0L16 9L0 18Z" fill="#fff"/></svg></div>
  </div>
</section>

<div class="tabs"><div class="wrap">
  <div class="tab active">Counselling Types</div>
  <div class="tab">Relationship Counselling Locations</div>
  <div class="tab">Sex Therapy Locations</div>
  <div class="tab">Quizzes</div>
  <div class="tab">F.A.Q.'s</div>
  <div class="tab">Contact</div>
</div></div>

<section class="types"><div class="wrap">
  <div class="type"><div class="type-photo" role="img" aria-label="Couple sharing a moment" style="background:linear-gradient(135deg,#e8cdb7,#b98d6c)"></div><h3>Relationship Counselling</h3><div class="need">Do you need help with:</div><p>Communication, Recovering from an affair, Loss of intimacy &amp; love, Power battles, Feeling like friends, not lovers</p></div>
  <div class="type"><div class="type-photo" role="img" aria-label="Intimate couple" style="background:linear-gradient(135deg,#f1ddd0,#cfa98f)"></div><h3>Sex Therapy Counselling</h3><div class="need">Do you need help with:</div><p>Low libido, Erectile difficulties, Premature ejaculation, Differing libidos, Porn addiction, Keeping sex exciting</p></div>
  <div class="type"><div class="type-photo" role="img" aria-label="Frustrated man" style="background:linear-gradient(135deg,#d6dde3,#8e9aa5)"></div><h3>Anger Management Counselling</h3><div class="need">Do you need help with:</div><p>Managing angry outbursts, expressing your anger in healthy ways</p></div>
  <div class="type"><div class="type-photo" role="img" aria-label="Confident woman" style="background:linear-gradient(135deg,#f0d6bf,#c9936d)"></div><h3>Narcissism Counselling</h3><div class="need">Do you need help with:</div><p>Managing narcissistic, superior, entitled, arrogant and lack of empathy tendencies in you or your partner</p></div>
</div></section>

<div class="wrap main">
  <main class="content">
    <h2>We Specialise in Relationship &amp; Marriage Counselling</h2>
    <p>At The Luma Haven, we are a group of <strong>PSYCHOLOGISTS</strong>, Australia wide who are <strong>passionate about relationships and helping you with yours.</strong></p>
    <p>Our vision is to provide the <strong>most highly regarded and comprehensive marriage counselling and relationship counselling, and sex therapy in Australia</strong>, at reasonable and affordable rates.</p>
    <p>When we are experiencing relationship and marriage problems, there can be a lot of pain and confusion, and it can often be difficult to cope with the other areas of our lives when we are struggling with problems with our partner.</p>
    <p>We are not taught about relationships and how to have a good one in our schools, so most of us are doing the best we know how, but <strong>lack the knowledge</strong> on how to create a better relationship.</p>

    <h2 style="margin-top:22px">Our Luma Haven Relationship Psychologists</h2>
    <p>Our team of 75 hand chosen <strong>Registered Psychologists</strong> in 60 locations Australia wide, are individually selected for their knowledge, experience, compassion, and unbiased approach to marriage counselling and sexual therapy.</p>
    <p>In addition all our Psychologists take part in our Initial Relationship Counselling Methodologies Training and yearly in-house conferences, ensuring you are in safe and experienced hands.</p>
    <p class="note">As we are Psychologists, so may be eligible for CareBack &amp; Private Health Insurance Rebates.<br>We are highly experienced and can help you with all kinds of relationship difficulties.</p>
    <p>Here are some of the common ones:</p>
    <ul class="checks">
      <li>Affairs</li><li>Controlling behaviour</li><li>Verbal abuse</li><li>Imbalance of power</li><li>Lack of intimacy</li><li>Poor communication</li><li>Loss of love</li><li>Relationship neglect</li><li>Sexual problems</li><li>Problems from childhood</li><li>Problems with parenting your children</li><li>Step children and in-laws</li><li>All forms of family problems</li><li>Anger management problems</li><li>Porn addiction problems</li><li>Pre-marriage programs</li><li>Narcissism problems</li>
    </ul>

    <div class="script">Our Relationship Counselling Approach</div>
    <p>It is an important part of our policy to take a very positive approach to our relationship counselling.</p>
    <p>We feel it is important to really understand the problems and perspectives of each of you, and at the same time, we find that most couples are looking to find a positive action plan and way through their problems to make changes which have a positive impact and a real sense of hope for their relationship.</p>
    <p class="note">Read more about our approach to counselling in our relationship counselling sessions, and frequently asked questions about the relationship and marriage counselling process.</p>
    <div class="ctas">
      <div class="cta"><div class="cta-photo" role="img" aria-label="Couple taking a quiz"></div><span>Take our Luma Relationship Assessment</span><i class="arrow"><svg width="8" height="10" viewBox="0 0 8 10"><path d="M1 1L6 5L1 9" stroke="#fff" stroke-width="2" fill="none"/></svg></i></div>
      <div class="cta"><div class="cta-photo" role="img" aria-label="Smiling psychologist"></div><span>Find out more about us</span><i class="arrow"><svg width="8" height="10" viewBox="0 0 8 10"><path d="M1 1L6 5L1 9" stroke="#fff" stroke-width="2" fill="none"/></svg></i></div>
    </div>

    <h2>Our Relationship Counselling Locations across Australia</h2>
    <p>We currently have relationship counselling and marriage counselling services in:</p>
    <ul class="locs">
      <li>Sydney – <b>19 centres</b></li><li>Adelaide – <b>4 centres</b></li>
      <li>Canberra – <b>2 centres</b></li><li>Gold Coast – <b>5 centres</b></li>
      <li>Melbourne – <b>21 centres</b></li><li>Sunshine Coast – <b>2 centres</b></li>
      <li>Perth – <b>11 centres</b></li><li>Cairns – <b>1 centre</b></li>
      <li>Brisbane – <b>14 centres</b></li><li>Townsville – <b>1 centre</b></li>
      <li>Wollongong – <b>1 centre</b></li><li>Wodonga – <b>1 centre</b></li>
      <li>Central Coast – <b>2 centres</b></li>
    </ul>
    <p>Certain clinics also provide <strong>after hours and Saturday sessions</strong> for your convenience. Click the Locations tab for more information about one of our caring psychologists in your area.</p>
    <div class="photo-wide" role="img" aria-label="Couple talking together on a sofa"></div>

    <div class="italic-h">Communication is a vital skill but not often taught to us.</div>
    <p>Most people find that their ways of communicating with each other are what hamper us from having a happy healthy relationship.</p>
    <p>Effective Interpersonal Communication skills are not something that we are usually taught. But for almost everyone who is having difficulties in their relationship, they feel that they are <strong>trying to communicate their thoughts and feelings but that their partner is not listening.</strong></p>
    <p>Most people then find that they, themselves don't want to listen when they experience their partner as not wanting to listen to them, so the net effect is that neither person gets listened to, and both are frustrated.</p>
    <p>So learning how to communicate your honest thoughts and feelings in a way that your partner does truly listen is a crucial skill for you to feel that you are in a fulfilling relationship. We can show you some simple but effective principles on how to do this with each other.</p>
    <div class="photo-small" role="img" aria-label="Woman listening thoughtfully"></div>

    <div class="italic-h">We as individuals have specific patterns in our relationships.</div>
    <p>We can also assist you if you want individual help and guidance on your relationship, so you can learn what the patterns in your relationship are showing you about yourself.</p>
    <p>If you have been in a number of relationships and have found yourself repeating the same kind of experiences, which is often the way our relationships play out, we can help you discover the patterns that you might be unwittingly setting up, so you can change these and move into more rewarding relationships in the future.</p>
    <p>Want more information? Please help yourself to our free articles on common relationship problems you may be encountering including:</p>
    <ul class="plain"><li>› Why relationships go wrong</li><li>› How to recover from an affair</li><li>› Have you lost yourself in your relationship</li><li>› The secret to more sex</li></ul>
    <p class="note">For the latest short, up-to-date articles on relationships, relationship problems and relationship counselling, please also check out our relationship counselling blog.</p>
  </main>

  <aside class="side">
    <div class="finder">
      <h4>Find Our Psychologist<br>Near You</h4>
      <div class="row"><label>Type of Counselling</label><span></span></div>
      <div class="row"><label>Location</label><span></span></div>
      <div class="or">OR</div>
      <div class="row"><label>Postcode</label><span></span></div>
      <div style="text-align:center"><span class="btn">SEARCH</span></div>
    </div>
    <div class="ad" role="img" aria-label="Stressed woman holding her head"><h5>Is Anxiety,<br>Depression<br>or Stress<br>bothering<br>YOU?</h5><div class="ad-bar">Click here for help from Luma Anxiety &amp; Depression Psychologists</div></div>
    <div class="ad gp" role="img" aria-label="Doctor with stethoscope"><h5>Information for referring GPs &amp; health professionals</h5><div class="ad-bar">Click here for more details</div></div>
    <h6>Rebates Available</h6>
    <div class="badges"><i style="background:#2e9d4a"></i><i style="background:#8b3a94"></i><i style="background:#2a7ec0"></i><i style="background:#cfd6dc"></i><i style="background:#1b5fa8"></i><i style="background:#4ab0d8"></i><i style="background:#5aa646"></i><i style="background:#e0e4e8"></i><i style="background:#2d7bb6"></i></div>
    <div class="more">plus many more</div>
    <p class="rebate">You may be able to receive rebates of up to <b>75% of your session costs</b> from CareBack or Private Health Insurers.</p>
    <div class="bar-btn">Click here for more details</div>
    <div class="sub">What To Expect From Counselling</div>
    <div class="vid" role="img" aria-label="Video of a counselling session"><i></i></div>
    <div class="blog-head">Our selection of blog posts on<b>Relationships &amp; Sex</b></div>
    <div class="post"><div class="thumb" role="img" aria-label="Blog photo"></div><div><b>What can I do if I'm living with a Narcissist?</b><small>February 24, 2017</small><em>Read More</em></div></div>
    <div class="post"><div class="thumb" role="img" aria-label="Blog photo"></div><div><b>Why am I with a Narcissist?</b><small>February 24, 2017</small><em>Read More</em></div></div>
    <div class="post"><div class="thumb" role="img" aria-label="Blog photo"></div><div><b>How Do I Know if I'm With a Narcissist?</b><small>February 24, 2017</small><em>Read More</em></div></div>
    <div class="post"><div class="thumb" role="img" aria-label="Blog photo"></div><div><b>Do You Wonder Why You and Your Partner Are Together?</b><small>October 19, 2016</small><em>Read More</em></div></div>
    <div class="post"><div class="thumb" role="img" aria-label="Blog photo"></div><div><b>Did Your Relationship Start on Rocky Ground?</b><small>October 12, 2016</small><em>Read More</em></div></div>
    <div class="post"><div class="thumb" role="img" aria-label="Blog photo"></div><div><b>What Are You Like In a Relationship?</b><small>October 5, 2016</small><em>Read More</em></div></div>
    <div class="post"><div class="thumb" role="img" aria-label="Blog photo"></div><div><b>Is Your Pursuit of Success Sabotaging Your Relationships That Matter Most?</b><small>September 28, 2016</small><em>Read More</em></div></div>
  </aside>
</div>

<section class="features"><div class="wrap">
  <div class="feat"><div class="ph" role="img" aria-label="Upset couple"></div><span>How to deal with an affair?</span><i class="arrow"></i></div>
  <div class="feat"><div class="ph" role="img" aria-label="Two men together"></div><span>Same Sex Relationships &amp; Counselling</span><i class="arrow"></i></div>
  <div class="feat"><div class="ph" role="img" aria-label="Woman looking in mirror"></div><span>Are you living with a narcissist?</span><i class="arrow"></i></div>
  <div class="feat"><div class="ph" role="img" aria-label="Couple turned away in bed"></div><span>Is one of you an Intimacy Withholder?</span><i class="arrow"></i></div>
  <div class="feat"><div class="ph" role="img" aria-label="Man at a laptop"></div><span>Is too much porn affecting your relationship?</span><i class="arrow"></i></div>
  <div class="feat"><div class="ph" role="img" aria-label="Worried woman"></div><span>Is your relationship safe? Is your partner controlling?</span><i class="arrow"></i></div>
</div></section>

<footer class="footer"><div class="wrap">
  <div class="top">
    <div><div class="name">THE LUMA HAVEN</div><div>CALL US ON 1300 555 014</div></div>
    <div class="login">MEMBER LOGIN <span>Email</span><span>Password</span><span class="go"></span></div>
  </div>
  <div class="copy">© Copyright The Luma Haven 2017 &nbsp; Visit us on www.TheLumaHaven.com.au<br>Privacy Policy | Terms &amp; Conditions | Site Map | Associate Psychologists Program | Contact Us</div>
</div></footer>

</body>
</html>
```